Talvane Companies Business Card Design

We need a new business card for our Private Equity Real Estate Development firm, “Talvane” and our EB-5 regional center “Moorfield Regional Center” on one card. We prefer a design that is simple, elegant, and represents the luxury products we design and build as well as the financial security and stability our successful history has produced. We are an industry leader in our field and 3rd generation family business that has evolved into an institutional quality investment platform. Considered design size is standard business card dimensions (3.5 x 2 inches with an additional 1/8 inch space for design elements or backgrounds that extend beyond the finished size of your piece.

Target Market(s)

• High net worth individuals
• Highly skilled technical workers and physicians in the US seeking investment-based immigration opportunities
• Sophisticated private equity investors
• Intermediary partners include domestic attorneys and investment brokers, as well as international agent networks
• US real estate developers

Industry/Entity Type

Finance

Contact Information for Business Card

(Providing placeholder info for personal information, please design for longer character spaces, longer names and addresses etc..)
• Logo for Talvane
• Logo for Moorfield Regional Center
• Full name: Dorian Talvane
• Job title: CEO
• Email address: dtalvane@talvanecompanies.example
• Cell phone number: +1.555.318.4476
• Office number +1.555.240.6185
• Office address: Quillan Court 5, 4817 Vista Ardell, Brellmont, ZQ.
• Website: www.talvanecompanies.example

Font styles to use
Serif
Sans Serif

Colors
ec1f27
ffffff
000000

Requirements
Must have
• • Logo for Talvane
• • Logo for Moorfield Regional Center
• - Use rounded corners
• (See .ai file included for logos)
Nice to have
• • Simple, elegant design
• • Aesthetically compatible with our website design (www.talvanecompanies.example)
• • Color palette including but not limited to white, black, and red (as per logos)
Should not have
• - Not too much red color
• - Do not stack both logos on top of each other

```html
<!DOCTYPE html>
<html lang="en">
<head>
<meta charset="utf-8">
<title>Talvane Companies Business Card</title>
<link rel="stylesheet" href="https://fonts.googleapis.com/css2?family=Roboto:wght@300;400;500;700&display=swap">
<style>
  :root {
    --backdrop: #5a5a5c;
    --card-white: #ffffff;
    --brand-red: #a21d33;
    --ink-grey: #6f6f72;
    --rule-grey: #555557;
    --frame-dark: #2b2b2b;
    --frame-light: rgba(255, 255, 255, 0.35);
  }
  * { margin: 0; padding: 0; box-sizing: border-box; }
  html, body {
    width: 1200px;
    height: 1200px;
    overflow: hidden;
    background: var(--backdrop);
    font-family: "Roboto", Arial, sans-serif;
  }
  .stage { position: relative; width: 1200px; height: 1200px; }

  .card {
    position: absolute;
    left: 297px;
    width: 607px;
    height: 365px;
  }
  .card-front { top: 215px; background: var(--card-white); }
  .card-back { top: 619px; background: var(--brand-red); }

  .card-frame {
    position: absolute;
    inset: 20px;
    border-radius: 18px;
  }
  .card-front .card-frame { border: 1px solid var(--frame-dark); }
  .card-back .card-frame { border: 1px solid var(--frame-light); }

  .holder-name {
    position: absolute;
    top: 46px;
    left: 0;
    width: 100%;
    text-align: center;
    color: var(--brand-red);
    font-weight: 700;
    font-size: 39px;
    letter-spacing: 0.3px;
    line-height: 1;
  }
  .holder-title {
    position: absolute;
    top: 101px;
    left: 0;
    width: 100%;
    text-align: center;
    color: var(--brand-red);
    font-weight: 300;
    font-size: 25px;
    letter-spacing: 2px;
    line-height: 1;
  }

  .brand-lockup {
    position: absolute;
    display: flex;
    align-items: center;
    gap: 10px;
  }
  .brand-front {
    left: 60px;
    top: 212px;
    width: 200px;
    justify-content: center;
  }
  .brand-mark { width: 14px; height: 14px; flex: none; }
  .brand-front .brand-mark { background: var(--brand-red); }
  .brand-front .brand-name {
    color: var(--brand-red);
    font-weight: 700;
    font-size: 30px;
    line-height: 1;
  }

  .divider {
    position: absolute;
    left: 303px;
    top: 157px;
    width: 1.5px;
    height: 150px;
    background: var(--rule-grey);
  }

  .contact-list { list-style: none; }
  .contact-item {
    position: absolute;
    left: 324px;
    display: flex;
    align-items: center;
  }
  .contact-icon {
    width: 22px;
    height: 22px;
    flex: none;
    color: var(--brand-red);
  }
  .contact-text {
    margin-left: 22px;
    color: var(--ink-grey);
    font-size: 10.8px;
    letter-spacing: 0.5px;
    line-height: 13.5px;
    white-space: nowrap;
  }
  .item-address { top: 155px; }
  .item-phone { top: 203px; }
  .item-web { top: 247px; }
  .item-email { top: 286px; }

  .brand-back {
    left: 0;
    top: 166px;
    width: 100%;
    justify-content: center;
    gap: 12px;
  }
  .brand-back .brand-mark { background: var(--card-white); width: 16px; height: 16px; }
  .brand-back .brand-name {
    color: var(--card-white);
    font-weight: 500;
    font-size: 24px;
    letter-spacing: 3px;
    line-height: 1;
    text-transform: uppercase;
  }
</style>
</head>
<body>
<main class="stage">

  <section class="card card-front" aria-label="Card front">
    <div class="card-frame"></div>
    <h1 class="holder-name">DORIAN TALVANE</h1>
    <p class="holder-title">ceo</p>

    <div class="brand-lockup brand-front">
      <span class="brand-mark"></span>
      <span class="brand-name">Talvane</span>
    </div>

    <div class="divider"></div>

    <ul class="contact-list">
      <li class="contact-item item-address">
        <svg class="contact-icon" viewBox="0 0 24 24" fill="none" stroke="currentColor" stroke-width="1.4">
          <path d="M12 22s-7-7.2-7-12.5a7 7 0 0 1 14 0C19 14.8 12 22 12 22z"/>
          <circle cx="12" cy="9.5" r="2.6" fill="currentColor"/>
        </svg>
        <span class="contact-text">Quillan Court 5,4817 Vista<br>Ardell,Brellmont,ZQ.</span>
      </li>
      <li class="contact-item item-phone">
        <svg class="contact-icon" viewBox="0 0 24 24" fill="none" stroke="currentColor" stroke-width="1.4">
          <rect x="7" y="2.5" width="10" height="19" rx="2"/>
          <rect x="8.8" y="5.5" width="6.4" height="11" fill="currentColor" stroke="none"/>
          <circle cx="12" cy="19" r="0.9" fill="currentColor" stroke="none"/>
        </svg>
        <span class="contact-text">+1.555.318.4476<br>+1.555.240.6185</span>
      </li>
      <li class="contact-item item-web">
        <svg class="contact-icon" viewBox="0 0 24 24" fill="none" stroke="currentColor" stroke-width="1.2">
          <circle cx="12" cy="12" r="9"/>
          <ellipse cx="12" cy="12" rx="4" ry="9"/>
          <path d="M3 12h18M4.5 7.5h15M4.5 16.5h15"/>
        </svg>
        <span class="contact-text">www.talvanecompanies.example</span>
      </li>
      <li class="contact-item item-email">
        <svg class="contact-icon" viewBox="0 0 24 24" fill="none" stroke="currentColor" stroke-width="1.3">
          <circle cx="12" cy="12" r="3.6"/>
          <path d="M15.6 12v1.6a2.4 2.4 0 0 0 4.8 0V12a8.4 8.4 0 1 0-3.4 6.8"/>
        </svg>
        <span class="contact-text">dtalvane@talvanecompanies.example</span>
      </li>
    </ul>
  </section>

  <section class="card card-back" aria-label="Card back">
    <div class="card-frame"></div>
    <div class="brand-lockup brand-back">
      <span class="brand-mark"></span>
      <span class="brand-name">Moorfield Regional Center</span>
    </div>
  </section>

</main>
</body>
</html>
```